Professional/modern business card design for construction company

We need a new business card design, double sided keeping it modern, sleek, professional and simple. We are an earthmoving business but do not want any pictures of machinery. I would like one side to have the logo and the other to have all the information, keeping with the colors in our logo. The business card will need to be able to be customised so we can use it for several different managers., we would also like to be able to use the design to apply it to other stationary ie. letterheads, notebooks etc. We do not really have a tag line but we could put on there that we specialise in - Agriculture, Civil Construction and Mining.

Contact Information for Business Card

Brolga Ridge Excavations Pty Ltd
ABN 58 402 937 615
82 Gumleaf Creek Road, Moree NSW 2400

Harold Benton
Managing Director
P 0418 639 204
E haroldbenton@brolgaridgeexc.com.au

Font styles to use
Serif
Sans Serif

Requirements
Nice to have
• I have attached some examples of ideas.
Should not have
• images of machinery

```html
<!DOCTYPE html>
<html lang="en">
<head>
<meta charset="utf-8">
<title>Brolga Ridge Excavations – Business Card</title>
<link href="https://fonts.googleapis.com/css2?family=Encode+Sans+Condensed:wght@400;600;700&family=Arimo:wght@400&display=swap" rel="stylesheet">
<style>
  :root {
    --orange: #f58a1f;
    --charcoal: #424242;
    --ink: #3a3a3a;
    --light-grey: #dadada;
    --panel-grey: #dcdcdc;
    --white: #ffffff;
  }
  * { margin: 0; padding: 0; box-sizing: border-box; }
  html, body { width: 1200px; height: 1000px; overflow: hidden; background: var(--white); }
  body { position: relative; font-family: "Encode Sans Condensed", "Arial Narrow", sans-serif; }

  .card { position: absolute; overflow: hidden; }

  /* Front */
  .card-front { left: 76px; top: 95px; width: 698px; height: 398px; background: var(--light-grey); }
  .card-front .lower { position: absolute; left: 0; top: 273px; width: 100%; height: 125px; background: var(--charcoal); }
  .card-front .accent-band {
    position: absolute; left: 0; top: 273px; width: 100%; height: 26px;
    background: linear-gradient(90deg, rgba(245,138,31,0) 2%, var(--orange) 22%, var(--orange) 78%, rgba(245,138,31,0) 98%);
  }
  .front-name {
    position: absolute; left: 0; right: 0; top: 110px; text-align: center;
    font-weight: 700; font-size: 46px; letter-spacing: 1px; color: var(--charcoal); line-height: 1;
  }

  /* Back */
  .card-back { left: 383px; top: 528px; width: 699px; height: 399px; background: var(--white); box-shadow: 0 2px 8px rgba(0,0,0,0.18); }
  .card-back .footer { position: absolute; left: 0; top: 272px; width: 100%; height: 127px; background: var(--panel-grey); }
  .card-back .accent-band {
    position: absolute; left: 0; top: 272px; width: 100%; height: 27px;
    background: linear-gradient(90deg, rgba(245,138,31,0) 2%, var(--orange) 24%, var(--orange) 76%, rgba(245,138,31,0) 98%);
  }
  .person-name {
    position: absolute; left: 0; right: 0; top: 40px; text-align: center;
    font-weight: 700; font-size: 38px; color: var(--orange); letter-spacing: 0.5px; line-height: 1;
  }
  .person-title {
    position: absolute; left: 0; right: 0; top: 80px; text-align: center;
    font-weight: 400; font-size: 21px; color: var(--orange); letter-spacing: 0.5px;
  }
  .contact-row {
    position: absolute; left: 50px; width: 600px; height: 45px;
    display: flex; align-items: center; justify-content: center; gap: 10px;
    background: linear-gradient(90deg, rgba(210,210,210,0) 0%, #d6d6d6 22%, #d6d6d6 78%, rgba(210,210,210,0) 100%);
    color: var(--ink); font-weight: 600;
  }
  .contact-row.phone { top: 135px; font-size: 32px; }
  .contact-row.email { top: 192px; font-size: 27px; }
  .contact-row svg { flex: none; }

  .footer-name {
    position: absolute; left: 78px; top: 318px;
    font-weight: 700; font-size: 25px; line-height: 1.05; color: var(--charcoal); letter-spacing: 0.5px;
  }
  .company-details {
    position: absolute; left: 308px; top: 318px;
    font-family: "Arimo", Arial, sans-serif; font-size: 15.5px; line-height: 20px; color: #2e2e2e;
  }
</style>
</head>
<body>

<section class="card card-front" aria-label="Business card front">
  <div class="lower"></div>
  <div class="accent-band"></div>
  <div class="front-name">BROLGA RIDGE EXCAVATIONS</div>
</section>

<section class="card card-back" aria-label="Business card back">
  <div class="person-name">HAROLD BENTON</div>
  <div class="person-title">Managing Director</div>

  <div class="contact-row phone">
    <svg width="34" height="34" viewBox="0 0 34 34" aria-hidden="true">
      <circle cx="17" cy="17" r="15.5" fill="none" stroke="var(--orange)" stroke-width="2"/>
      <path d="M11.5 9.5c1-.8 2-.6 2.6.3l1.6 2.5c.5.8.3 1.7-.4 2.2l-1 .7c.7 2 2.3 3.9 4.3 5l.8-.9c.6-.7 1.5-.8 2.2-.3l2.5 1.7c.8.6 1 1.6.3 2.5l-.9 1.1c-1 1.2-2.9 1.4-5 .3-3.5-1.8-6.5-5.3-7.9-9.1-.7-2-.3-3.7.9-4.6z" fill="none" stroke="var(--orange)" stroke-width="1.6" stroke-linejoin="round"/>
    </svg>
    <span>0418 639 204</span>
  </div>

  <div class="contact-row email">
    <svg width="34" height="34" viewBox="0 0 34 34" aria-hidden="true">
      <circle cx="17" cy="17" r="15.5" fill="none" stroke="var(--orange)" stroke-width="2"/>
      <rect x="8.5" y="11.5" width="17" height="11" fill="none" stroke="var(--orange)" stroke-width="1.5"/>
      <path d="M8.5 11.5l8.5 6.5 8.5-6.5M8.5 22.5l6-5M25.5 22.5l-6-5" fill="none" stroke="var(--orange)" stroke-width="1.3"/>
    </svg>
    <span>haroldbenton@brolgaridgeexc.com.au</span>
  </div>

  <div class="footer"></div>
  <div class="accent-band"></div>
  <div class="footer-name">BROLGA RIDGE<br>EXCAVATIONS</div>
  <div class="company-details">
    <p>Brolga Ridge Excavations Pty Ltd</p>
    <p>ABN 58 402 937 615</p>
    <p>82 Gumleaf Creek Road, Moree NSW 2400</p>
  </div>
</section>

</body>
</html>
```